New boutique IT consultancy needs business card

I need a business card and logo for my IT consultancy business, called 'Quenbrylle' . I want it to make me look bigger than I am. I want it to look classy, and modern. Simple design, that will be easy for me to translate into my webpage etc. The business card should be bold, and different.

The logo should emphasise the 'y' as used in quenbrylle

Target Market(s)

IT divisions in other companies

Industry/Entity Type

Business

Contact Information for Business Card

Marcel Thornby
Director
+61 437 819 063
mthornby@quenbrylle-mail.com

```html
<!DOCTYPE html>
<html lang="en">
<head>
<meta charset="utf-8">
<title>Quenbrylle — Business Card</title>
<link rel="stylesheet" href="https://fonts.googleapis.com/css2?family=Open+Sans:wght@300;400;700&display=swap">
<style>
  :root {
    --backdrop: #3b3430;
    --card: #0c0c0c;
    --card-edge: #1a1a1a;
    --accent-blue: #1a7fd4;
    --ink-white: #f2f2f2;
    --silver: #cfcfcf;
    --divider: #1f4f78;
  }
  * { box-sizing: border-box; margin: 0; padding: 0; }
  html, body {
    width: 1200px; height: 900px; overflow: hidden;
    background: var(--backdrop);
    font-family: "Open Sans", sans-serif;
  }
  .stage { position: relative; width: 1200px; height: 900px; }
  .card {
    position: absolute; top: 290px;
    width: 545px; height: 320px;
    background: var(--card);
    border: 1px solid var(--card-edge);
    border-radius: 4px;
    box-shadow: 0 10px 28px rgba(0,0,0,0.45);
  }
  /* Front side */
  .card-front { left: 35px; }
  .front-brand {
    position: absolute; left: 28px; top: 150px;
    width: 250px; height: 100px;
    display: flex; align-items: center;
  }
  .brand-name {
    font-weight: 700; font-size: 44px; color: var(--ink-white);
    line-height: 1; letter-spacing: -0.5px;
  }
  .front-divider {
    position: absolute; left: 290px; top: 110px;
    width: 1px; height: 100px; background: var(--divider);
  }
  .contact-block { position: absolute; left: 305px; top: 96px; }
  .person-name {
    font-weight: 700; font-size: 17px; color: var(--accent-blue); line-height: 1.2;
  }
  .person-role { font-size: 13px; color: var(--ink-white); margin-top: 2px; }
  .contact-list { list-style: none; margin-top: 16px; }
  .contact-list li {
    display: flex; align-items: center; gap: 9px;
    font-size: 13px; color: var(--ink-white); line-height: 20px;
    white-space: nowrap;
  }
  .contact-list svg { width: 11px; height: 11px; fill: var(--accent-blue); flex: none; }
  /* Back side */
  .card-back {
    left: 620px;
    display: flex; align-items: center; justify-content: center;
  }
  .back-name {
    font-weight: 300; font-size: 42px; color: var(--silver);
    letter-spacing: 1px; text-transform: uppercase; line-height: 1;
  }
</style>
</head>
<body>
<main class="stage">
  <section class="card card-front" aria-label="Business card front">
    <div class="front-brand">
      <span class="brand-name">Quenbrylle</span>
    </div>
    <span class="front-divider"></span>
    <div class="contact-block">
      <p class="person-name">Marcel Thornby</p>
      <p class="person-role">Director</p>
      <ul class="contact-list">
        <li>
          <svg viewBox="0 0 16 16" aria-hidden="true"><path d="M3.5 1.5l2.5 0 1.2 3.2-1.6 1.3c.9 1.9 2.4 3.4 4.3 4.3l1.3-1.6 3.2 1.2v2.5c0 .9-.8 1.6-1.7 1.6C7 14 2 9 1.9 3.2 1.9 2.3 2.6 1.5 3.5 1.5z"/></svg>
          +61 437 819 063
        </li>
        <li>
          <svg viewBox="0 0 16 16" aria-hidden="true"><path d="M1 3h14v10H1z M1.8 3.8L8 8.8l6.2-5H1.8z" fill-rule="evenodd"/></svg>
          mthornby@quenbrylle-mail.com
        </li>
        <li>
          <svg viewBox="0 0 16 16" aria-hidden="true"><circle cx="8" cy="8" r="7"/></svg>
          www.quenbrylle.com
        </li>
      </ul>
    </div>
  </section>

  <section class="card card-back" aria-label="Business card back">
    <span class="back-name">Quenbrylle</span>
  </section>
</main>
</body>
</html>
```